Corbel Path Advisory WordPress Design

Corbel Path Advisory is a consulting company that targets small business. We use our genius in the field to help small Business navigate information systems, in particular Tallybridge Solutions.

We are looking for a WordPress Design that is playful but intelligent for our web site. The design should plays off of our Corbel Logo and be informative. The attachments is of our logo variations that will be used in your design. It should be useful to describe the look and feel of the site we are looking to get.

The color of the website is not defined yet but should work well with our logo colors.

Regarding to the template and the way to display the home page. The menu should contain the following items which will each be its own page:
1. Home Page
2. Blog
-This needs to be a frame work to allow us to constantly add written articles and Video logs with Transcripts possibly in two sections.
3. What Corbel Does
-This will contain the company approach
4. Request a Corbel
-This will be a form to collect contact information
5. Contact Corbel
6. About Us

Please keep the SIMILAR airy/mythical design used in the logo.

Finally, we need a design that will have a normal view and a mobile view.

Target Market(s)

Corbel Path Advisory is a consulting company that targets small business.

Industry/Entity Type

Business Consultant

Requirements
Must have
• Regarding to the template and the way to display the home page. The menu should contain the following items which will each be its own page:
• 1. Home Page
• 2. Blog
• -This needs to be a frame work to allow us to constantly add written articles and Video logs with Transcripts possibly in two sections.
• 3. What Corbel Does
• -This will contain the company approach
• 4. Request a Corbel
• -This will be a form to collect contact information
• 5. Contact Corbel
• 6. About Us
• Mobile View
Nice to have
• Have a magical or mythical quality like the hands around the logo but not to playful.
Should not have
• Our slogan is "Corbel solutions that make business work!"

```html
<!DOCTYPE html>
<html lang="en">
<head>
<meta charset="utf-8">
<title>Corbel Path Advisory — Home</title>
<link href="https://fonts.googleapis.com/css2?family=Open+Sans:wght@400;600;700;800&display=swap" rel="stylesheet">
<style>
:root{
  --orange:#f39c1f;
  --ink:#222;
  --hero:#1d1d1f;
  --hero-2:#2c2c2e;
  --text:#6a6a6a;
  --muted:#9a9a9a;
  --grey-bg:#f1f1f1;
  --icon-grey:#6b6b6b;
  --footer:#262626;
  --white:#fff;
}
*{margin:0;padding:0;box-sizing:border-box}
html,body{width:1200px;height:2392px;overflow:hidden;background:var(--white)}
body{font-family:"Open Sans",Arial,sans-serif;color:var(--text);position:relative}
.abs{position:absolute}

/* hero */
.hero{position:absolute;left:0;top:0;width:1200px;height:720px;background:linear-gradient(180deg,var(--hero-2),var(--hero));overflow:hidden}
.hero-photo{position:absolute;left:560px;top:110px;width:580px;height:610px;background:radial-gradient(ellipse at 50% 40%,#6b6460 0%,#3a3633 45%,#1d1d1f 80%)}
.hero-wave{position:absolute;left:0;bottom:0}
.topbar{position:absolute;top:18px;left:560px;display:flex;gap:10px;align-items:center;font-size:13px;color:#bbb}
.topbar .dot{width:26px;height:26px;border:1px solid #777;border-radius:50%}
.topbar .contact{margin-left:26px}
.nav{position:absolute;left:260px;top:78px;width:840px;height:50px;background:var(--orange);display:flex}
.nav a{color:var(--white);text-decoration:none;font-size:13px;font-weight:600;text-transform:uppercase;display:flex;align-items:center;justify-content:center;flex:1;letter-spacing:.3px;white-space:nowrap}
.nav a.active{background:var(--ink);flex:.7}
.brand{position:absolute;left:100px;top:30px;width:160px;height:175px;background:#111;border:2px solid #444;display:flex;flex-direction:column;align-items:center;justify-content:center;gap:14px}
.brand .mark{width:62px;height:62px;border-radius:50%;background:var(--orange)}
.brand .name{color:var(--white);font-weight:700;font-size:17px;line-height:1.2;text-align:center}
.hero-kicker{left:100px;top:372px;color:var(--white);font-size:24px;font-weight:400;line-height:1.3}
.hero-title{left:100px;top:406px;color:var(--orange);font-size:44px;font-weight:800;letter-spacing:.5px;line-height:1.2}
.hero-copy{left:100px;top:472px;width:440px;color:#ddd;font-size:13px;line-height:1.6}
.btn{display:inline-flex;align-items:center;gap:10px;background:var(--orange);color:var(--white);font-size:13px;font-weight:700;text-transform:uppercase;padding:0 22px;height:42px;border-radius:3px;white-space:nowrap}
.btn .arr{width:18px;height:18px;border-radius:50%;background:var(--white);position:relative}
.btn .arr::after{content:"";position:absolute;left:6px;top:5px;border-left:7px solid var(--orange);border-top:4px solid transparent;border-bottom:4px solid transparent}
.hero-btn{left:100px;top:548px}
.dots{left:100px;top:624px;display:flex;gap:8px}
.dots i{width:11px;height:11px;border-radius:50%;background:#777}
.dots i.on{background:var(--orange)}

/* features */
.feature{position:absolute;top:800px;width:300px;text-align:center}
.feature .circle{width:96px;height:96px;border-radius:50%;background:var(--icon-grey);margin:0 auto 26px;display:flex;align-items:center;justify-content:center}
.feature .circle.hot{background:var(--orange)}
.feature h3{font-size:17px;font-weight:600;color:#444;margin-bottom:10px}
.feature p{font-size:13px;line-height:1.6;color:var(--muted)}

/* welcome */
.welcome{position:absolute;left:0;top:1060px;width:1200px;height:470px;background:var(--grey-bg)}
.welcome h2{position:absolute;top:48px;width:100%;text-align:center;font-size:42px;font-weight:700;color:#555}
.welcome h2 span{color:var(--orange)}
.welcome p{position:absolute;top:120px;left:100px;width:1000px;text-align:center;font-size:14px;line-height:1.7;color:var(--text)}
.welcome .scene{position:absolute;left:210px;top:225px;width:780px;height:120px;background:linear-gradient(90deg,#c9cde9,#dfe2f0,#c9cde9);border-radius:6px}
.welcome .btn{position:absolute;left:540px;top:385px}

/* know more */
.know{position:absolute;top:1600px;left:100px;width:310px}
.know h2{font-size:27px;font-weight:700;color:#444;line-height:1.1}
.know h4{font-size:22px;font-weight:600;color:var(--orange);margin:4px 0 20px}
.know p{font-size:13px;line-height:1.65;color:var(--muted)}
.know .more{margin-top:20px;font-size:12px;font-weight:700;color:#444;display:flex;align-items:center;gap:10px}
.know .more i{width:16px;height:16px;border-radius:50%;background:#444}
.card{position:absolute;top:1600px;width:210px}
.card .photo{height:180px}
.card h5{font-size:15px;font-weight:600;color:#444;margin:16px 0 6px}
.card p{font-size:12px;line-height:1.6;color:var(--muted)}

/* blog */
.blog-title{position:absolute;left:100px;top:1948px;font-size:20px;font-weight:700;color:#444}
.post{position:absolute;top:2010px;width:500px;height:170px}
.post .photo{position:absolute;left:0;top:0;width:195px;height:165px}
.post .body{position:absolute;left:215px;top:0;width:275px}
.post h5{font-size:15px;font-weight:600;color:#444;line-height:1.35}
.post .date{font-size:12px;color:var(--orange);font-weight:600;margin:8px 0}
.post p{font-size:12px;line-height:1.6;color:var(--muted)}
.post .rm{margin-top:10px;font-size:12px;font-weight:700;color:#444}

/* footer */
.footer{position:absolute;left:0;top:2250px;width:1200px;height:142px;background:var(--footer);color:#bbb}
.footer h6{font-size:16px;font-weight:700;color:var(--white);margin-bottom:8px}
.footer .col{position:absolute;top:30px;font-size:12px;line-height:1.7}
.footer .follow{position:absolute;left:866px;top:44px;display:flex;align-items:center;gap:8px}
.footer .follow b{font-size:17px;color:var(--white);margin-right:10px;font-weight:700}
.footer .follow i{width:24px;height:24px;background:var(--white);border-radius:3px}
</style>
</head>
<body>

<header class="hero">
  <div class="hero-photo" role="img" aria-label="Photo of a confident businessman in a dark suit and red tie"></div>
  <div class="topbar">
    <span class="dot"></span><span class="dot"></span><span class="dot"></span><span class="dot"></span>
    <span class="contact">+1 (555) 014 2270</span>
    <span class="contact">hello@corbelpath.com</span>
  </div>
  <nav class="nav">
    <a class="active">Home</a>
    <a>About Us</a>
    <a>What Corbel Does</a>
    <a>Request a Corbel</a>
    <a>Blog</a>
    <a>Contact Corbel</a>
  </nav>
  <div class="brand">
    <span class="mark"></span>
    <span class="name">Corbel Path<br>Advisory</span>
  </div>
  <div class="abs hero-kicker">Corbel Path Advisory</div>
  <div class="abs hero-title">SMALL BUSINESS</div>
  <p class="abs hero-copy">Clear guidance for owners who want their systems to simply work.<br>We map, simplify and support your Tallybridge tools step by step.</p>
  <div class="abs btn hero-btn">Know More <span class="arr"></span></div>
  <div class="abs dots"><i class="on"></i><i></i><i></i><i></i></div>
  <svg class="hero-wave" width="1200" height="90" viewBox="0 0 1200 90"><path d="M0 60 C300 10 600 10 840 40 C1000 60 1120 50 1200 20 L1200 90 L0 90Z" fill="#fff"/></svg>
</header>

<section>
  <div class="feature" style="left:102px">
    <div class="circle"><svg width="40" height="48" viewBox="0 0 40 48"><rect x="4" y="2" width="32" height="44" rx="4" fill="none" stroke="#fff" stroke-width="3"/><rect x="10" y="9" width="20" height="26" fill="#fff"/><circle cx="20" cy="40" r="2" fill="#fff"/></svg></div>
    <h3>Small Business</h3>
    <p>We help small teams choose, set up and run the<br>tools they rely on, with plain advice that<br>saves time and money.</p>
  </div>
  <div class="feature" style="left:450px">
    <div class="circle hot"><svg width="50" height="44" viewBox="0 0 50 44"><rect x="3" y="3" width="44" height="28" rx="2" fill="none" stroke="#fff" stroke-width="3"/><rect x="21" y="31" width="8" height="7" fill="#fff"/><rect x="14" y="38" width="22" height="3" fill="#fff"/></svg></div>
    <h3>Small Business</h3>
    <p>Practical Tallybridge training for your staff so<br>every person knows where things live and<br>how work moves forward.</p>
  </div>
  <div class="feature" style="left:798px">
    <div class="circle"><svg width="48" height="44" viewBox="0 0 48 44"><circle cx="18" cy="24" r="10" fill="none" stroke="#fff" stroke-width="6" stroke-dasharray="5 3"/><circle cx="18" cy="24" r="4" fill="#fff"/><circle cx="36" cy="12" r="6" fill="none" stroke="#fff" stroke-width="4" stroke-dasharray="3 2"/><circle cx="37" cy="33" r="5" fill="none" stroke="#fff" stroke-width="4" stroke-dasharray="3 2"/></svg></div>
    <h3>Small Business</h3>
    <p>Ongoing support when things change, from new<br>workflows to clean permissions and<br>reliable everyday reports.</p>
  </div>
</section>

<section class="welcome">
  <h2>WELCOME TO <span>CORBEL PATH ADVISORY</span></h2>
  <p>Corbel Path Advisory is a consulting company for small business. We bring deep experience with information systems, and Tallybridge Solutions in particular, to help you work smarter. Our approach is calm and clear: we listen first, learn how your team works, then shape tools that fit, always without the jargon or the stress.</p>
  <div class="scene" role="img" aria-label="Illustration of meditating figures linked by small idea and screen icons"></div>
  <div class="btn">Read More <span class="arr"></span></div>
</section>

<section>
  <div class="know">
    <h2>GET TO KNOW MORE</h2>
    <h4>What Corbel Does</h4>
    <p>We review how your business stores and shares information, then build a simple plan. Each step is explained so your team stays confident. When the work is done, we stay close to answer questions and keep everything running smoothly as you grow.</p>
    <div class="more">READ MORE <i></i></div>
  </div>
  <div class="card" style="left:432px">
    <div class="photo" role="img" aria-label="Photo of two business people shaking hands" style="background:linear-gradient(135deg,#cfd3d8,#8a8f96)"></div>
    <h5>Clear plans for teams</h5>
    <p>Short guides that turn complex systems into simple daily steps.</p>
  </div>
  <div class="card" style="left:660px">
    <div class="photo" role="img" aria-label="Photo of a team meeting around a laptop" style="background:linear-gradient(135deg,#e4e6ea,#6d7580)"></div>
    <h5>Training that sticks</h5>
    <p>Hands-on sessions so your people learn by doing real work.</p>
  </div>
  <div class="card" style="left:896px">
    <div class="photo" role="img" aria-label="Photo of a person on a mountain top at sunrise" style="background:linear-gradient(180deg,#d9c8a8,#8c7c66)"></div>
    <h5>Support as you grow</h5>
    <p>We stay beside you when goals shift and needs expand.</p>
  </div>
</section>

<section>
  <div class="blog-title">LATEST BLOG</div>
  <article class="post" style="left:100px">
    <div class="photo" role="img" aria-label="Photo of hands joined together over a table" style="background:radial-gradient(circle,#b9b2a6,#6e655a)"></div>
    <div class="body">
      <h5>Five quick ways to tidy your shared files this month</h5>
      <div class="date">JULY 22, 2015</div>
      <p>A simple checklist to clear clutter, fix folder names and help everyone find the right document fast.</p>
      <div class="rm">READ MORE ›</div>
    </div>
  </article>
  <article class="post" style="left:600px">
    <div class="photo" role="img" aria-label="Photo of two colleagues reviewing work at a desk" style="background:linear-gradient(135deg,#dfe3e8,#7c8694)"></div>
    <div class="body">
      <h5>Video log: setting up your first team workspace</h5>
      <div class="date">JULY 18, 2015</div>
      <p>Watch the walkthrough and read the transcript to build a clean, shared space for your whole team.</p>
      <div class="rm">READ MORE ›</div>
    </div>
  </article>
</section>

<footer class="footer">
  <div class="col" style="left:100px">
    <h6>COPYRIGHT</h6>
    © 2015 Corbel Path Advisory. All rights reserved.<br>
    Home &nbsp;|&nbsp; Blog &nbsp;|&nbsp; What Corbel Does &nbsp;|&nbsp; About Us
  </div>
  <div class="col" style="left:456px">
    <h6>ADDRESS</h6>
    Corbel Path Advisory 418 Meridian Ave, Fairhaven, OR 97301<br>
    (555) 018 4433
  </div>
  <div class="follow"><b>FOLLOW US</b><i></i><i></i><i></i></div>
</footer>

</body>
</html>
```